Coffee House With Cycling Theme Wants Business Cards

We want to create a business card for a coffee house that has a cycling theme. We expect to use the current logo on one side of the business card and we have been considering adding the words 'COFFEE HOUSE' underneath (see example). For the other side of the business card we want an interesting design with tag-line, address and social media links (the normal business card stuff). See examples provided but we are not fixed on having it exactly as shown, we are very open to great creative ideas. Please note our logo has the initials ‘RM' in orange embedded in the design and this must be retained. However, you can play with the words COFFEE HOUSE as well as use the orange color on the backside of the business card, as you see fit. For an image on the backside of the business card it can be a photo, hand-drawn or whatever but it must visually combine coffee and cycling in some way. The interior of the Coffee House will be reclaimed wood, rustic and have an urban feel to it with cycling artifacts hanging from the walls/ceiling, etc. Finally, it would be beneficial if the business card design elements can be easily used on flyers and other promotional assets. Good luck, we are looking forward to seeing your creative ideas.

Target Market(s)

Coffee lovers and cycling fans

Contact Information for Business Card

See project description.

Colors

Designer to choose colors to be used in the design.

Requirements
Must have
• Must use the current logo provided and combine a coffee and bike theme.
Nice to have
• Orange is used in current logo and could be used as an accent color on the backside of the business card.

```html
<!DOCTYPE html>
<html lang="en">
<head>
<meta charset="utf-8">
<title>RM Coffee House – Business Card Back</title>
<link rel="stylesheet" href="https://fonts.googleapis.com/css2?family=Oxygen:wght@400;700&display=swap">
<style>
  :root {
    --stage: #e9e6e2;
    --card: #000000;
    --accent: #ff6a1a;
    --muted: #474747;
    --label: #4f4f4f;
  }
  * { box-sizing: border-box; margin: 0; padding: 0; }
  html, body {
    width: 1200px;
    height: 686px;
    overflow: hidden;
    background: var(--stage);
  }
  body {
    display: flex;
    align-items: center;
    justify-content: center;
    font-family: "Oxygen", "Helvetica Neue", Arial, sans-serif;
  }
  .card {
    position: relative;
    width: 1000px;
    height: 647px;
    background: var(--card);
    text-align: center;
  }
  .tagline {
    position: absolute;
    top: 34px;
    left: 0;
    right: 0;
    color: var(--accent);
    font-size: 68px;
    font-weight: 400;
    line-height: 1;
    letter-spacing: 0.5px;
  }
  .address {
    position: absolute;
    top: 222px;
    left: 0;
    right: 0;
    color: var(--muted);
    font-style: normal;
    font-size: 64px;
    line-height: 78px;
    letter-spacing: 1.5px;
  }
  .links {
    position: absolute;
    top: 458px;
    left: 0;
    right: 0;
    list-style: none;
  }
  .link {
    position: absolute;
    top: 0;
    width: 300px;
    margin-left: -150px;
    display: flex;
    flex-direction: column;
    align-items: center;
  }
  .link--web { left: 174px; }
  .link--social-a { left: 499px; }
  .link--social-b { left: 842px; }
  .link-icon {
    width: 97px;
    height: 97px;
    display: block;
  }
  .link-square {
    width: 97px;
    height: 97px;
    border-radius: 12px;
    background: var(--muted);
  }
  .link-label {
    margin-top: 14px;
    color: var(--label);
    font-size: 27px;
    letter-spacing: 0.5px;
    line-height: 1.2;
  }
</style>
</head>
<body>
  <main class="card">
    <h1 class="tagline">TAGLINE, TAGLINE, TAGLINE</h1>

    <address class="address">
      STREET ADDRESS LINE 1<br>
      STREET ADDRESS LINE 2
    </address>

    <ul class="links">
      <li class="link link--web">
        <svg class="link-icon" viewBox="0 0 100 100" aria-hidden="true" fill="none" stroke="var(--muted)" stroke-width="6">
          <circle cx="50" cy="50" r="45"/>
          <ellipse cx="50" cy="50" rx="20" ry="45"/>
          <line x1="50" y1="5" x2="50" y2="95"/>
          <line x1="5" y1="50" x2="95" y2="50"/>
          <path d="M12 28 H88 M12 72 H88"/>
        </svg>
        <span class="link-label">rmcoffeehouse.com</span>
      </li>
      <li class="link link--social-a">
        <span class="link-square" aria-hidden="true"></span>
        <span class="link-label">rmcoffeehouse</span>
      </li>
      <li class="link link--social-b">
        <span class="link-square" aria-hidden="true"></span>
        <span class="link-label">rmcoffeehouse</span>
      </li>
    </ul>
  </main>
</body>
</html>
```